Web Design Project

need a website, logo and a matching business Card for design studio. i have a company that works with many companies and i want to offer design services that will be outsourced to craftflock.

this website is totally for the design services. i need it to be simple but very catcgy and trendy, yet MUST BE ELEGENT.

you being a designer will know best what do i require in this website and how it should look and feel..

i dont need many pages, most of the selling work to clients will be face to face, this is just for them to view the sample works.

the company is called "Corvelin, Vividra Studio", so pages i need are: 1- the Studio 2- Folios 3- Contact us( will include company informaiton, and online contact form that should have a drop-down list of all types of designs.

main focus is the folios pages, it needs to have samples of works, the classification of works should be on two basis, by type of design and by designer. client should be able to select a certain designer and send an inquiry. if the customer does that, then i should get all client details and the designer should get a notification that he has been requested though no contact details of client should be given to designer as i want to make sure that those jobs are given to designer through craft flock and this is an invitation for any designer who care to put his works on the website. next to that, if the customer requires a job online then we need to get information on how design should feel and look.

please quote your price to include the website and business card design, A3 head letter and envelope.

Please provide a mock up of your design or a briefing an initial design before asking to be announced as the winner.

my customers are general managers and decision makers.

Business

• ability to filiter works based on type or designer. and website must offer all types of designs included here

```html
<!DOCTYPE html>
<html lang="en">
<head>
<meta charset="utf-8">
<title>Corvelin Vividra Studio</title>
<link rel="stylesheet" href="https://fonts.googleapis.com/css2?family=Arimo:wght@400;700&family=Josefin+Sans:wght@300&family=Monoton&family=Bowlby+One+SC&family=Open+Sans:ital,wght@0,400;0,600;1,400&display=swap">
<style>
  :root {
    --paper: #ebe9e2;
    --panel: #ffffff;
    --ink: #333333;
    --nav-ink: #454545;
    --line: #e3e3e3;
    --accent: #d8322a;
    --link: #e8501a;
    --hero-top: #f7f7f7;
    --hero-bottom: #ebebeb;
    --sky: #d8eef9;
    --social-a: #8fa7d8;
    --social-b: #8fd2ef;
    --badge: #f6f2ea;
  }
  * { box-sizing: border-box; margin: 0; padding: 0; }
  html, body { width: 1200px; height: 1073px; overflow: hidden; }
  body {
    position: relative;
    background: var(--paper);
    font-family: "Arimo", Arial, sans-serif;
    color: var(--ink);
  }
  .page-panel {
    position: absolute; left: 47px; top: 68px; width: 1106px; height: 934px;
    background: var(--panel);
    box-shadow: 0 8px 10px -4px rgba(0,0,0,.35);
  }
  .brand {
    position: absolute; left: 50%; top: 22px; transform: translateX(-50%);
    background: var(--panel); border-radius: 30px;
    padding: 8px 34px 10px;
    font-family: "Arimo", Arial, sans-serif; font-weight: 700;
    font-size: 58px; line-height: 1; color: var(--ink); white-space: nowrap;
  }
  .main-nav {
    position: absolute; left: 70px; top: 128px; width: 1059px; height: 59px;
    border: 1px solid var(--line); display: flex; align-items: stretch;
  }
  .main-nav a {
    display: flex; align-items: center; padding: 0 25px;
    border-right: 1px solid var(--line);
    font-size: 27px; font-weight: 700; color: var(--nav-ink); text-decoration: none;
  }
  .social {
    margin-left: auto; display: flex; align-items: center; gap: 6px; padding-right: 9px;
  }
  .social-label {
    font-family: "Open Sans", sans-serif; font-style: italic; font-size: 14px;
    color: #5a6a70; margin-right: 12px;
  }
  .social-square { width: 38px; height: 38px; }
  .social-square.one { background: var(--social-a); }
  .social-square.two { background: var(--social-b); }

  .hero {
    position: absolute; left: 70px; top: 216px; width: 1059px; height: 438px;
    background: linear-gradient(var(--hero-top), var(--hero-bottom));
    box-shadow: 0 16px 14px -12px rgba(0,0,0,.35);
    overflow: hidden;
  }
  .hero-line {
    position: absolute; left: 36px; white-space: nowrap; line-height: 1;
  }
  .hero-line.top {
    top: 160px; font-family: "Josefin Sans", sans-serif; font-weight: 300;
    font-size: 60px; color: #2b2b2b; letter-spacing: 0;
  }
  .hero-line.bottom {
    top: 222px; font-family: "Monoton", sans-serif; font-size: 66px;
    color: var(--accent); letter-spacing: 0;
  }
  .hero-art {
    position: absolute; left: 638px; top: 6px; width: 384px; height: 414px;
    border-radius: 50% 50% 40% 40%;
    background: radial-gradient(circle at 50% 42%, #ffffff 0 38%, var(--sky) 39% 52%, transparent 53%),
                radial-gradient(ellipse at 50% 95%, #e2e2e2 0 30%, transparent 60%);
  }

  .services {
    position: absolute; left: 70px; top: 654px; width: 1059px; height: 324px;
    background: linear-gradient(#ffffff, #ececec);
  }
  .carousel-arrow {
    position: absolute; top: 156px; width: 16px; height: 24px;
  }
  .carousel-arrow.prev { left: 8px; }
  .carousel-arrow.next { left: 1036px; }
  .service {
    position: absolute; top: 54px; width: 226px;
  }
  .service-card {
    position: relative; height: 202px; background: var(--panel);
    border: 1px solid #e6e6e6;
  }
  .service-title {
    position: absolute; top: 10px; left: 0; right: 0; text-align: center;
    font-family: "Bowlby One SC", sans-serif; font-size: 23px;
    color: var(--accent); letter-spacing: -0.5px;
  }
  .price-badge {
    position: absolute; left: 14px; top: 60px; width: 115px; height: 115px;
    border-radius: 50%; background: radial-gradient(circle at 50% 35%, #ffffff, var(--badge));
    box-shadow: 0 2px 6px rgba(0,0,0,.2); border: 4px solid #fff;
    text-align: center;
  }
  .price-from {
    display: block; margin-top: 24px; font-family: "Open Sans", sans-serif;
    font-style: italic; font-size: 15px; color: #777;
  }
  .price-amount {
    display: block; font-family: "Arimo", Arial, sans-serif; font-weight: 700;
    font-size: 34px; color: #2a2a2a; line-height: 1.1;
  }
  .service-thumb {
    position: absolute; border-radius: 2px;
  }
  .thumb-splat { left: 124px; top: 146px; width: 84px; height: 70px; border-radius: 45%; background: var(--accent); }
  .thumb-cards { left: 108px; top: 138px; width: 110px; height: 76px; background: linear-gradient(#ffffff, #eeeeee); box-shadow: 0 1px 4px rgba(0,0,0,.3); }
  .thumb-stationery { left: 126px; top: 138px; width: 90px; height: 76px; background: linear-gradient(#ffffff, #f1efe8); box-shadow: 0 1px 4px rgba(0,0,0,.3); }
  .thumb-site { left: 136px; top: 138px; width: 82px; height: 76px; background: linear-gradient(#ffffff, #e9eef2); box-shadow: 0 1px 4px rgba(0,0,0,.3); }
  .learn-more {
    position: relative; z-index: 1;
    display: block; margin: 26px auto 0; width: 104px; height: 22px;
    border: 1px solid #c8c8c8; border-radius: 11px;
    background: linear-gradient(#ffffff, #e6e6e6);
    font-size: 13px; line-height: 20px; text-align: center; color: #444; text-decoration: none;
  }

  .site-footer {
    position: absolute; left: 0; top: 1028px; width: 1200px; text-align: center;
    font-family: "Open Sans", sans-serif; font-weight: 600; font-size: 12.5px; color: #222;
  }
  .site-footer a { color: var(--link); text-decoration: none; }
</style>
</head>
<body>
  <div class="page-panel"></div>
  <div class="brand">Corvelin Vividra Studio</div>

  <nav class="main-nav">
    <a href="#">The Studio</a>
    <a href="#">Folios</a>
    <a href="#">Contact Us</a>
    <div class="social">
      <span class="social-label">Join Us</span>
      <span class="social-square one"></span>
      <span class="social-square two"></span>
    </div>
  </nav>

  <section class="hero">
    <div class="hero-line top">YOUR BUSINESS</div>
    <div class="hero-line bottom">OUR CREATIVITY</div>
    <div class="hero-art" role="img" aria-label="Illustration of a leafy sapling growing out of a USB plug in front of a pale blue circle"></div>
  </section>

  <section class="services">
    <svg class="carousel-arrow prev" viewBox="0 0 16 24"><polyline points="12,3 4,12 12,21" fill="none" stroke="#333" stroke-width="1.6"/></svg>
    <svg class="carousel-arrow next" viewBox="0 0 16 24"><polyline points="4,3 12,12 4,21" fill="none" stroke="#333" stroke-width="1.6"/></svg>

    <div class="service" style="left:44px">
      <div class="service-card">
        <div class="service-title">Logo Design</div>
        <div class="price-badge"><span class="price-from">Starting at</span><span class="price-amount">$240</span></div>
        <div class="service-thumb thumb-splat" role="img" aria-label="Red paint splat illustration"></div>
      </div>
      <a class="learn-more" href="#">Learn More</a>
    </div>

    <div class="service" style="left:294px">
      <div class="service-card">
        <div class="service-title">Business Card</div>
        <div class="price-badge"><span class="price-from">Starting at</span><span class="price-amount">$130</span></div>
        <div class="service-thumb thumb-cards" role="img" aria-label="Sample business cards"></div>
      </div>
      <a class="learn-more" href="#">Learn More</a>
    </div>

    <div class="service" style="left:542px">
      <div class="service-card">
        <div class="service-title">Stationery</div>
        <div class="price-badge"><span class="price-from">Starting at</span><span class="price-amount">$200</span></div>
        <div class="service-thumb thumb-stationery" role="img" aria-label="Sample letterhead and envelopes"></div>
      </div>
      <a class="learn-more" href="#">Learn More</a>
    </div>

    <div class="service" style="left:790px">
      <div class="service-card">
        <div class="service-title">Web Design</div>
        <div class="price-badge"><span class="price-from">Starting at</span><span class="price-amount">$320</span></div>
        <div class="service-thumb thumb-site" role="img" aria-label="Sample website layout"></div>
      </div>
      <a class="learn-more" href="#">Learn More</a>
    </div>
  </section>

  <footer class="site-footer">
    Copyright © 2012 Corvelin Vividra Studio. Use of this website constitutes acceptance of our <a href="#">User Agreement</a>, <a href="#">Privacy Policy</a> and <a href="#">money back refund policy.</a>
  </footer>
</body>
</html>
```